The Web Promotion Playbook for Yard & Patio Construction Crews

We need a book cover design that is for a book targeting landscape and outdoor living contractors that helps them grow their business using online marketing.

We run a business focused on this industry so you can see what we do: https://yardcrewgrowthworks.com/

The title is: The Web Promotion Playbook for Yard & Patio Construction Crews

The author is: Trent Varnholm
Some drafts have been done however they're still looking basic and somewhat amateur, we're looking for something that will stand out.

Target Market(s)

Landscape, Hardscape and Outdoor Living Contractors and Business Owners

Industry/Entity Type

Online Marketing

Font styles to use
Serif
Sans Serif

Requirements
Must have
• The part of the title that should stand out the most is the text "Web Promotion Playbook".
Should not have
• The color red

```html
<!DOCTYPE html>
<html lang="en">
<head>
<meta charset="utf-8">
<title>The Web Promotion Playbook for Yard &amp; Patio Construction Crews — Book Cover</title>
<link href="https://fonts.googleapis.com/css2?family=Oswald:wght@700&display=swap" rel="stylesheet">
<style>
  :root {
    --backdrop: #7d9b50;
    --cover-green: #89ac5a;
    --cover-green-deep: #7c9f4f;
    --gold-light: #f9de50;
    --gold-mid: #f2bc2c;
    --gold-deep: #e29a1a;
    --title-white: #f4f4f1;
    --rule-dark: #2d3a1f;
    --foliage: #a3c63e;
    --foliage-deep: #5f8a2a;
    --canopy: #eee6cf;
    --furniture: #34402f;
    --stone-light: #e2cf9e;
    --stone: #c9ab74;
    --stone-deep: #a98b5a;
    --shadow: rgba(30, 40, 15, 0.55);
  }
  * { margin: 0; padding: 0; box-sizing: border-box; }
  html, body {
    width: 1200px; height: 1200px; overflow: hidden;
    background: var(--backdrop);
  }
  .cover {
    position: absolute; left: 200px; top: 0;
    width: 800px; height: 1200px; overflow: hidden;
    background: linear-gradient(180deg, var(--cover-green) 0%, var(--cover-green-deep) 100%);
    font-family: "Oswald", "Impact", sans-serif;
    font-weight: 700;
    text-align: center;
  }
  .cover-photo {
    position: absolute; left: 0; right: 0; top: 670px; bottom: 0;
    background:
      linear-gradient(180deg, rgba(137,172,90,1) 0%, rgba(137,172,90,0) 12%),
      linear-gradient(180deg,
        var(--foliage) 0%,
        var(--canopy) 13%,
        var(--foliage) 27%,
        var(--foliage-deep) 47%,
        var(--furniture) 62%,
        var(--stone-light) 70%,
        var(--stone) 82%,
        var(--stone-deep) 100%);
  }
  .book-title { font-weight: 700; }
  .title-kicker, .title-main {
    display: block;
    background: linear-gradient(180deg, var(--gold-light) 0%, var(--gold-mid) 55%, var(--gold-deep) 100%);
    -webkit-background-clip: text; background-clip: text;
    color: transparent;
    filter: drop-shadow(2px 3px 2px var(--shadow));
  }
  .title-kicker {
    position: absolute; top: 48px; left: 0; right: 0;
    font-size: 74px; line-height: 1.15;
  }
  .title-main {
    position: absolute; top: 128px; left: 0; right: 0;
    font-size: 150px; line-height: 1.15; letter-spacing: 3px;
  }
  .title-connector {
    position: absolute; top: 318px; left: 85px; right: 85px;
    display: flex; align-items: center; gap: 22px;
  }
  .title-connector .rule { flex: 1; height: 3px; background: var(--rule-dark); }
  .title-connector .word {
    font-size: 46px; line-height: 1.1; color: var(--gold-mid);
    text-shadow: 2px 2px 2px var(--shadow);
  }
  .title-subject {
    position: absolute; top: 384px; left: 0; right: 0;
    color: var(--title-white);
    font-size: 80px; line-height: 94px;
    text-shadow: 3px 4px 4px var(--shadow);
  }
  .author {
    position: absolute; bottom: 30px; left: 0; right: 0;
    color: var(--title-white);
    font-size: 54px; line-height: 1.1; letter-spacing: 0.5px;
    text-shadow: 3px 3px 5px rgba(0,0,0,0.7);
  }
</style>
</head>
<body>
  <main class="cover">
    <div class="cover-photo" role="img" aria-label="Photo of a sunny outdoor patio terrace with cream umbrellas, wicker lounge furniture, palms and a stone paved floor"></div>
    <h1 class="book-title">
      <span class="title-kicker">The Web Promotion</span>
      <span class="title-main">PLAYBOOK</span>
      <span class="title-connector"><span class="rule"></span><span class="word">for</span><span class="rule"></span></span>
      <span class="title-subject">Yard &amp; Patio<br>Construction<br>Crews</span>
    </h1>
    <p class="author">Trent Varnholm</p>
  </main>
</body>
</html>
```